KWR CONSTRUCTION CO POSTCARD DESIGN

I was thinking of making a postcard for mailings by printmeadow and or by me dropping off at homes . I guess it would be used as a mailing post card and or flyer . I have had sketch harbor design my buisnes cards . The buisness card design is a different version from my signage on trucks because of space . I have a logo design . thyat i can upload . I like silver for back ground and black for logo and letters with glossy finish . I would like to have the KWR with a back drop to give it depth , it would be the same color as windows .

The file i submitted ha a design with red letters , this design is more detailed than the other and should be used . The colors should be black on a silver card glossy . The windows and maybe give the letters depth with a backdrop outline . I want to let home owners know that they can always call for consultation and and repairs or maintenance for their home .

Target Market(s)

home owners

Industry/Entity Type

Construction

Font styles to use
Other font styles liked:
• The same font as used in the picture of the sign i uploaded

Requirements
Must have
• HOME IMPROVEMENTS , MAINTENANCE AND REPAIRS , CARPENTRY , TILE PAINTING ECT

```html
<!DOCTYPE html>
<html lang="en">
<head>
<meta charset="UTF-8">
<title>KWR Construction Co. Postcard</title>
<link rel="stylesheet" href="https://fonts.googleapis.com/css2?family=Crimson+Text:wght@400;600;700&display=swap">
<style>
  :root {
    --backdrop: #3a3029;
    --silver: #c3c3c3;
    --ink: #0b0b0b;
    --band-text: #a9a9a9;
    --rule-grey: #7d7d7d;
    --light-text: #e2e2e2;
  }
  * { margin: 0; padding: 0; box-sizing: border-box; }
  html, body { width: 1200px; height: 1000px; overflow: hidden; }
  body {
    background: var(--backdrop);
    font-family: "Crimson Text", "Times New Roman", serif;
    color: var(--ink);
    position: relative;
  }
  .card {
    position: absolute;
    background: var(--silver);
  }

  /* Front side */
  .card-front { left: 305px; top: 8px; width: 561px; height: 484px; }
  .front-frame {
    position: absolute; inset: 5px;
    border: 2px solid var(--ink);
  }
  .reg-number {
    position: absolute; left: 20px; top: 20px;
    font-size: 13px; letter-spacing: 0.3px;
  }
  .header-rule {
    position: absolute; left: 7px; right: 7px; top: 183px;
    height: 6px; background: var(--ink);
  }
  .header-rule-thin {
    position: absolute; left: 18px; right: 12px; top: 196px;
    height: 2px; background: var(--rule-grey);
  }
  .name-band {
    position: absolute; left: 17px; right: 10px; top: 202px; height: 48px;
    background: var(--ink);
    display: flex; align-items: center; justify-content: center;
  }
  .brand-name {
    color: var(--band-text);
    font-weight: 400;
    font-size: 42px;
    letter-spacing: 0.5px;
    line-height: 1;
    white-space: nowrap;
  }
  .front-contact {
    position: absolute; left: 0; right: 0; top: 266px;
    text-align: center;
  }
  .front-contact .person { font-size: 33px; letter-spacing: 1px; line-height: 40px; }
  .front-contact .phone { font-size: 24px; line-height: 30px; margin-top: 10px; }
  .front-contact .web, .front-contact .address { font-size: 20px; line-height: 30px; letter-spacing: 0.4px; }
  .services-bar {
    position: absolute; left: 7px; right: 7px; top: 442px; height: 24px;
    background: var(--ink);
    color: var(--light-text);
    font-size: 12.5px; letter-spacing: 0.3px;
    display: flex; align-items: center; justify-content: center;
    white-space: nowrap;
  }

  /* Back side */
  .card-back { left: 305px; top: 508px; width: 563px; height: 484px; }
  .back-brand {
    position: absolute; left: 13px; top: 14px; width: 406px; height: 140px;
    background: var(--ink);
    border-right: 2px solid var(--rule-grey);
    display: flex; flex-direction: column; align-items: center; justify-content: center;
    color: var(--band-text); font-weight: 400; line-height: 1;
  }
  .back-brand .brand-initials { font-size: 68px; letter-spacing: 1px; }
  .back-brand .brand-rest { font-size: 38px; margin-top: 6px; }
  .stamp-box {
    position: absolute; left: 423px; top: 14px; width: 125px; height: 140px;
    border: 2px solid var(--ink);
  }
  .sender {
    position: absolute; left: 10px; width: 246px; top: 215px;
    text-align: center;
  }
  .sender .person { font-size: 24px; letter-spacing: 1px; line-height: 32px; }
  .sender .phone { font-size: 18px; line-height: 24px; margin-top: 10px; }
  .sender .web { font-size: 15px; line-height: 24px; margin-top: 6px; }
  .address-area { position: absolute; left: 0; top: 0; }
</style>
</head>
<body>

  <section class="card card-front">
    <div class="front-frame"></div>
    <p class="reg-number">HOME IMPROVEMENT REG # 205731</p>
    <div class="header-rule"></div>
    <div class="header-rule-thin"></div>
    <div class="name-band">
      <span class="brand-name">KWR CONSTRUCTION CO.</span>
    </div>
    <div class="front-contact">
      <p class="person">DAN MORELLI</p>
      <p class="phone">555-014-2738</p>
      <p class="web">WWW.KWRCONSTRUCTIONCO.COM</p>
      <p class="address">27 ALDER ROW MILLBROOK MA. 01999</p>
    </div>
    <div class="services-bar">HOME IMPROVEMENTS , MAINTENANCE AND REPAIRS , CARPENTRY , TILE PAINTING</div>
  </section>

  <section class="card card-back">
    <div class="back-brand">
      <span class="brand-initials">KWR</span>
      <span class="brand-rest">CONSTRUCTION CO.</span>
    </div>
    <div class="stamp-box"></div>
    <div class="sender">
      <p class="person">DAN MORELLI</p>
      <p class="phone">555-014-2738</p>
      <p class="web">WWW.KWRCONSTRUCTIONCO.COM</p>
    </div>
    <svg class="address-area" width="563" height="484" viewBox="0 0 563 484" aria-hidden="true">
      <line x1="272" y1="185" x2="272" y2="385" stroke="#7d7d7d" stroke-width="2"/>
      <line x1="278" y1="222" x2="543" y2="222" stroke="#7d7d7d" stroke-width="2"/>
      <line x1="278" y1="268" x2="543" y2="268" stroke="#7d7d7d" stroke-width="2"/>
      <line x1="278" y1="313" x2="543" y2="313" stroke="#7d7d7d" stroke-width="2"/>
    </svg>
  </section>

</body>
</html>
```